Software company design for letters and quotations

Clean modern design. Colors & logo are available on our website.
www.tralvexsoft.be

Target Market(s)

business clients

Industry/Entity Type

Business Software

Requirements
Must have
• delivery as word templates & psd

```html
<!DOCTYPE html>
<html lang="en">
<head>
<meta charset="utf-8">
<title>Tralvex Software – Letterhead</title>
<link href="https://fonts.googleapis.com/css2?family=Open+Sans:wght@400;700&family=Reenie+Beanie&display=swap" rel="stylesheet">
<style>
  :root {
    --bg: #e3e3e3;
    --paper: #ffffff;
    --brand-blue: #0b5f93;
    --accent-blue: #2ea6de;
    --text: #3c3c3c;
    --muted: #555555;
  }
  * { box-sizing: border-box; margin: 0; padding: 0; }
  html, body { width: 1200px; height: 968px; overflow: hidden; }
  body {
    background: var(--bg);
    font-family: "Open Sans", Arial, sans-serif;
    color: var(--text);
    position: relative;
  }
  address { font-style: normal; }
  .letterhead {
    position: absolute;
    left: 290px; top: 45px;
    width: 620px; height: 877px;
    background: var(--paper);
    box-shadow: 0 6px 22px rgba(0,0,0,0.18);
    overflow: hidden;
  }
  .brand {
    position: absolute; left: 58px; top: 56px;
    display: flex; align-items: center; gap: 8px;
  }
  .brand-square { width: 14px; height: 14px; background: var(--brand-blue); }
  .brand-name {
    font-weight: 700; font-size: 19px; letter-spacing: 0.5px;
    color: var(--brand-blue);
  }
  .recipient {
    position: absolute; left: 58px; top: 112px;
    font-size: 10.5px; line-height: 15px; color: var(--muted);
  }
  .sender {
    position: absolute; right: 58px; top: 112px;
    font-size: 10.5px; line-height: 15px; color: var(--muted);
  }
  .sender .line { display: flex; align-items: center; gap: 5px; }
  .sender svg { width: 10px; height: 10px; }
  .date {
    position: absolute; right: 58px; top: 206px;
    font-size: 10.5px; color: var(--muted);
  }
  .body-copy {
    position: absolute; left: 58px; top: 236px; width: 504px;
    font-size: 10.5px; line-height: 14.5px; color: var(--text);
  }
  .body-copy p { margin-bottom: 10px; }
  .signoff { position: absolute; left: 58px; top: 568px; }
  .signature {
    font-family: "Reenie Beanie", cursive;
    font-size: 36px; line-height: 30px; color: #1e1e1e;
  }
  .signer-role { font-size: 10px; color: var(--muted); margin-top: 2px; }
  .footer-band { position: absolute; left: 0; bottom: 0; width: 620px; height: 200px; }
  .footer-url {
    position: absolute; left: 40px; bottom: 28px;
    font-size: 12px; letter-spacing: 3px; color: #ffffff;
  }
</style>
</head>
<body>
  <main class="letterhead">
    <header class="brand">
      <span class="brand-square"></span>
      <span class="brand-name">TRALVEX SOFTWARE</span>
    </header>

    <address class="recipient">
      Recipient's Name<br>
      Recipient's Title<br>
      Recipient's Company<br>
      Recipient's Company Address
    </address>

    <address class="sender">
      <div>Kaaistraat 12,</div>
      <div>2000 Antwerpen, België</div>
      <div class="line">
        <svg viewBox="0 0 10 10"><circle cx="5" cy="5" r="4.4" fill="none" stroke="#555" stroke-width="0.9"/><path d="M3.6 3 L4.4 3 L4.7 4 L4.2 4.4 Q4.8 5.5 5.6 5.9 L6 5.4 L7 5.7 L7 6.5 Q4 6.8 3.6 3 Z" fill="#555"/></svg>
        +32(0)3 555.01.20
      </div>
      <div class="line">
        <svg viewBox="0 0 10 10"><circle cx="5" cy="5" r="4.4" fill="none" stroke="#555" stroke-width="0.9"/><rect x="3" y="3.6" width="4" height="2.8" fill="none" stroke="#555" stroke-width="0.6"/><path d="M3 3.6 L5 5.1 L7 3.6" fill="none" stroke="#555" stroke-width="0.6"/></svg>
        info@tralvexsoft.be
      </div>
    </address>

    <p class="date">Kaaistraat January, 2016</p>

    <section class="body-copy">
      <p>Lorem Ipsum is simply dummy text of the printing and typesetting industry. Lorem Ipsum has been the industry's standard dummy text ever since the 1500s, when an unknown printer took a galley of type and scrambled it to make a type specimen book. It has survived not only five centuries, but also the leap into electronic typesetting, remaining essentially unchanged. It was popularised in the 1960s with the release of Transfera sheets containing Lorem Ipsum passages, and more recently with desktop publishing software like PageForge Studio including versions of Lorem Ipsum.</p>
      <p>The standard chunk of Lorem Ipsum used since the 1500s is reproduced below for those interested. Sections 1.10.32 and 1.10.33 from "de Rebus Ordinandis" by M. Veldan are also reproduced in their exact original form, accompanied by English versions from the 1914 translation by J. Morrow</p>
      <p>Lorem Ipsum is simply dummy text of the printing and typesetting industry. Lorem Ipsum has been the industry's standard dummy text ever since the 1500s, when an unknown printer took a galley of type and scrambled it to make a type specimen book. It has survived not only five centuries, but also the leap into electronic typesetting, remaining essentially unchanged. It was popularised in the</p>
      <p>The standard chunk of Lorem Ipsum used since the 1500s is reproduced below for those interested. Sections 1.10.32 and 1.10.33 from "de Rebus Ordinandis" by M. Veldan are also reproduced in their exact original form, accompanied by English versions from the 1914 translation by J. Morrow.</p>
    </section>

    <div class="signoff">
      <div class="signature">your name</div>
      <div class="signer-role">Company Director</div>
    </div>

    <svg class="footer-band" viewBox="0 0 620 200" preserveAspectRatio="none">
      <path d="M0 14 C 280 34, 500 90, 610 200" fill="none" stroke="var(--accent-blue)" stroke-width="3"/>
      <path d="M0 26 C 270 46, 480 104, 590 200 L0 200 Z" fill="var(--brand-blue)"/>
    </svg>
    <p class="footer-url">www.tralvexsoft.be</p>
  </main>
</body>
</html>
```